Whitening Pen artwork design

Whitening Pens with silkscreen printing:
sample: https://www.shopmarrow.example/Toviqa-Whitening-Carbamide-Sensitivity-Travel-Friendly/dp/K93R4T8W1Q/ref=sr_1_5?dchild=1&keywords=whitening+pen&qid=1728301944&sr=8-5

inside the writing:
"teeth whitening pen " change to "BRISK WHITENING PEN"
"logo" change to our logo

requirements:
Inches: 1.77" wide x 1.57" around
CM: 4.5cm wide x 4cm around

See attached file Generic Pen Artwork Placement Silkscreen – this is not a template, just a guideline, refer to the exact sizing above

- An "identifying marker" is required: Teeth Whitening Pen or Teeth Whitening Gel (for example)

-We require PDF files created to print ready specifications. Color images should be down-sampled to 300DPI

-Please provide us your Hueledger color reference for the color used in your artwork

https://www.hueledger.example/color-finder#/pick?swatchBook=solidCoatedV3M2

-Please ensure that all fonts are embedded in the PDF document or make sure you convert fonts to outlines to prevent any issues with fonts (AI-Type-Create Outlines)

We will need your print ready artwork in a high resolution PDF file

```html
<!DOCTYPE html>
<html lang="en">
<head>
<meta charset="utf-8">
<title>BRISK Whitening Pen – Silkscreen Artwork</title>
<link rel="stylesheet" href="https://fonts.googleapis.com/css2?family=Cinzel:wght@700;900&family=Marcellus&family=Montserrat:wght@600;700&family=Pinyon+Script&display=swap">
<style>
  :root {
    --navy: #13388a;
    --gold: #9b782f;
    --silver: #c9c9cb;
    --lilac: #c695c6;
    --white: #ffffff;
    --ink: #111111;
    --pink: #e0368f;
    --pink-tint: #fbeef5;
    --blue: #123c8d;
    --blue-tint: #eeeff8;
    --label-border: #c8c8c8;
  }
  * { margin: 0; padding: 0; box-sizing: border-box; }
  html, body { width: 1200px; height: 849px; overflow: hidden; background: var(--white); }
  .artboard { position: relative; width: 1200px; height: 849px; }

  /* ---------- Bright White wrap ---------- */
  .wrap-banner {
    position: absolute; left: 162px; top: 181px; width: 810px; height: 179px;
    background: var(--navy); overflow: hidden;
  }
  .wrap-banner .shapes { position: absolute; inset: 0; }
  .new-flag {
    position: absolute; left: 8px; top: 25px; transform: rotate(-45deg);
    font: 700 24px/1 "Montserrat", sans-serif; color: var(--white); letter-spacing: 0.5px;
  }
  .brand-mark {
    position: absolute; display: flex; align-items: center; gap: 7px;
    font-family: "Montserrat", sans-serif; font-weight: 700; letter-spacing: 1.5px;
    line-height: 1;
  }
  .brand-mark .dot { border-radius: 50%; flex: none; }
  .wrap-banner .brand-mark { left: 89px; top: 22px; font-size: 29px; color: var(--lilac); }
  .wrap-banner .brand-mark .dot { width: 19px; height: 19px; background: var(--lilac); }
  .product-name {
    position: absolute; left: 46px; top: 53px;
    font: 900 62px/1 "Cinzel", serif; color: var(--white); letter-spacing: 0;
    transform: scaleX(0.82); transform-origin: left top;
  }
  .product-script {
    position: absolute; left: 292px; top: 44px;
    font: 400 78px/1 "Pinyon Script", cursive; color: var(--white);
  }
  .product-line {
    position: absolute; left: 46px; top: 120px;
    font: 400 29px/1 "Marcellus", serif; color: var(--white); letter-spacing: 0.5px;
    -webkit-text-stroke: 0.6px var(--white);
  }
  .volume {
    position: absolute; right: 14px; top: 137px;
    font: 600 12.5px/1 "Montserrat", sans-serif; color: var(--white);
  }
  .claim {
    position: absolute; right: 9px; top: 157px;
    font: 700 13.5px/1 "Marcellus", serif; color: var(--ink); letter-spacing: 1.3px;
  }

  /* ---------- Identifier labels ---------- */
  .id-label {
    position: absolute; left: 162px; width: 455px; height: 118px;
    border: 1px solid var(--label-border); overflow: hidden;
  }
  .id-label--pen { top: 397px; color: var(--pink); }
  .id-label--gel { top: 538px; color: var(--blue); }
  .id-label .pattern-area { position: absolute; inset: 0; }
  .id-label--pen .pattern-area { background: var(--pink-tint); }
  .id-label--gel .pattern-area { background: var(--blue-tint); }
  .id-label .brand-mark { left: 23px; top: 10px; font-size: 26px; color: currentColor; }
  .id-label .brand-mark .dot { width: 17px; height: 17px; background: currentColor; }
  .id-label .line-name {
    position: absolute; left: 21px; top: 30px;
    font: 400 84px/1 "Marcellus", serif; letter-spacing: 0;
    -webkit-text-stroke: 2.4px currentColor;
    transform: scaleX(0.84); transform-origin: left top;
  }
  .id-label .type-word {
    position: absolute; left: 232px;
    font: 400 35px/1 "Marcellus", serif; -webkit-text-stroke: 1px currentColor;
  }
  .id-label .type-word--top { top: 40px; }
  .id-label .type-word--bottom { top: 73px; }
  .id-label .type-rule {
    position: absolute; left: 300px; top: 98px; width: 125px; height: 3px; background: currentColor;
  }
</style>
</head>
<body>
<main class="artboard">

  <section class="wrap-banner" aria-label="Bright White pen wrap">
    <svg class="shapes" viewBox="0 0 810 179" width="810" height="179" aria-hidden="true">
      <polygon points="0,0 95,0 0,102" fill="var(--gold)"/>
      <path d="M195,179 C470,158 640,70 810,0 L810,3 C650,72 480,162 215,179 Z" fill="var(--silver)"/>
      <path d="M265,179 C540,150 690,55 810,11 L810,179 Z" fill="var(--gold)"/>
    </svg>
    <span class="new-flag">NEW</span>
    <div class="brand-mark"><span class="dot"></span>SOLVANE</div>
    <h1 class="product-name">BRIGHT</h1>
    <span class="product-script">White</span>
    <p class="product-line">BRISK WHITENING PEN</p>
    <p class="volume">0.07 FL.OZ(2ML)</p>
    <p class="claim">PROFESSIONAL LEVEL WHITENING GUARANTEED</p>
  </section>

  <section class="id-label id-label--pen" aria-label="Whitening pen identifier">
    <div class="pattern-area" role="img" aria-label="Soft repeating heart pattern background"></div>
    <div class="brand-mark"><span class="dot"></span>SOLVANE</div>
    <h2 class="line-name">BRISK</h2>
    <span class="type-word type-word--top">WHITENING</span>
    <span class="type-word type-word--bottom">PEN</span>
    <span class="type-rule"></span>
  </section>

  <section class="id-label id-label--gel" aria-label="Whitening gel identifier">
    <div class="pattern-area" role="img" aria-label="Soft repeating heart pattern background"></div>
    <div class="brand-mark"><span class="dot"></span>SOLVANE</div>
    <h2 class="line-name">BRISK</h2>
    <span class="type-word type-word--top">WHITENING</span>
    <span class="type-word type-word--bottom">GEL</span>
    <span class="type-rule"></span>
  </section>

</main>
</body>
</html>
```